Website for boutique digital agency helping high-tech startups accelerate growth.

We need a website design for a relatively young company based in Mauritius called 'LumaTrel'.

We are a professional services firm delivering digital infrastructure for revenue operations (RevOps)*.

Entrepreneurial startups and SMBs in the technology sector work with us to accelerate growth by delivering extraordinary customer experiences across the full customer lifecycle.

We would like a colourful design that utilises the (4) colours of our existing logo design.

The final design should communicate dynamic growth through relentless customer focus.
----------------------------------------------------------
*Revenue Operations (RevOps) is the strategic alignment of sales, marketing and customer success operations to accelerate growth by delivering extraordinary customer experiences across the full customer life cycle.

Target Market(s)

Entrepreneurial startups and SMBs (Small/Medium Businesses) in the technology sector.

Question: Why the technology sector?

Answer: Because technology entrepreneurs often have a tremendous challenge to effectively communicate to the market and to prospective customers the value and the benefits of their products & services due to the inherent complexity of technological innovation.

LumaTrel is a team of creatively-minded engineers and technologists who have worked with and understand the technologies and innovations our clients are passionate about bringing to market.

Industry/Entity Type

Professional Service

Number of Pages Required

5+ page

Font styles to use
Sans Serif

Requirements
Must have
• Minimalistic designs rich with visual meaning are highly preferred. Mobile responsive designs are also required. Must show how designs render on Desktop, Tablet and Smartphone devices.

Website pages:
1) Homepage: problem statement, target customers, value proposition & benefits
2) Services: 3-4 tiers of services packages with pricing and "how to work with us"
3) Resources: links to all kinds of relevant materials
4) Contact Us: contact form and special project quote form
5) Blog: matrix design with featured images for each post
Nice to have
• Bold, interesting, colourful, inspiring images that visually communicate:
- relentless customer focus
- extraordinary, memorable experiences
- business at the speed of innovation
Should not have
• Any meme or theme that panders to "political correctness".

```html
<!DOCTYPE html>
<html lang="en">
<head>
<meta charset="utf-8">
<title>LumaTrel – Boutique Digital Agency</title>
<link href="https://fonts.googleapis.com/css2?family=Montserrat:wght@400;600;700;800&family=Open+Sans:wght@400;600;700&display=swap" rel="stylesheet">
<style>
:root{
  --red:#e3262d;
  --orange:#f0421f;
  --green:#78b52a;
  --blue:#1c96d4;
  --teal:#176775;
  --charcoal:#2c2f31;
  --footer:#1d1e20;
  --ink:#222528;
  --muted:#7b7f83;
  --line:#e4e4e4;
  --white:#ffffff;
}
*{margin:0;padding:0;box-sizing:border-box}
html,body{width:1200px;height:3708px;overflow:hidden;background:var(--white)}
body{font-family:"Open Sans",Arial,sans-serif;color:var(--ink)}
.page{position:relative;width:1200px;height:3708px;overflow:hidden}
.abs{position:absolute}
h1,h2,h3,h4,.brand,.btn,.nav a{font-family:"Montserrat",Arial,sans-serif}

/* buttons */
.btn{display:inline-flex;align-items:center;gap:8px;background:var(--orange);color:var(--white);
  font-size:13px;font-weight:700;letter-spacing:.5px;text-transform:uppercase;text-decoration:none;
  padding:14px 26px;border-radius:30px;box-shadow:0 4px 10px rgba(240,66,31,.3)}
.btn .dot{width:16px;height:16px;border-radius:50%;background:var(--white);display:inline-flex;align-items:center;justify-content:center}

/* brand */
.brand{display:flex;align-items:center;gap:10px;font-weight:800;color:var(--red);text-decoration:none}
.brand .mark{border-radius:50%;background:var(--green)}

/* header */
.topline{left:0;top:0;width:1200px;height:6px;background:var(--red)}
.header{left:0;top:6px;width:1200px;height:106px;background:var(--white);display:flex;align-items:center;padding:0 140px}
.header .brand{font-size:30px}
.header .brand .mark{width:26px;height:26px}
.nav{margin-left:auto;display:flex;align-items:center;gap:40px}
.nav a{font-size:14px;font-weight:700;color:var(--ink);text-decoration:none}
.nav a.active{color:var(--red);border-bottom:3px solid var(--red);padding-bottom:6px}
.nav .btn{padding:12px 28px}

/* hero */
.hero{left:0;top:112px;width:1200px;height:660px}
.hero-photo{position:absolute;inset:0;background:linear-gradient(100deg,#eef1f3 0%,#d9dfe3 35%,#9fa9b1 60%,#6e7882 100%)}
.hero-copy{left:120px;top:120px;width:470px}
.hero-copy h1{font-size:38px;line-height:1.2;font-weight:800;color:var(--ink)}
.hero-copy p{margin:22px 0 32px;font-size:15px;line-height:1.6;color:#444;width:380px}
.hero-arrow{top:300px;width:40px;height:40px;border-radius:50%;background:rgba(255,255,255,.75);display:flex;align-items:center;justify-content:center}
.hero-v{left:0;top:0}

/* welcome */
.welcome{left:0;top:760px;width:1200px;text-align:center}
.welcome .mark-big{margin:0 auto;width:76px;height:76px;border-radius:50%;background:var(--white);box-shadow:0 2px 10px rgba(0,0,0,.12);display:flex;align-items:center;justify-content:center}
.welcome .mark-big span{width:40px;height:40px;border-radius:50%;background:var(--green)}
.welcome h2{margin-top:20px;font-size:40px;font-weight:800}
.welcome p{width:760px;margin:22px auto 30px;font-size:14px;line-height:1.8;color:var(--muted)}
.divider{left:0;top:1120px;width:1200px;height:1px;background:var(--line)}

/* problem */
.problem-photo{left:112px;top:1188px;width:448px;height:324px;background:linear-gradient(135deg,#e9e5df,#b9b3aa 55%,#7b756d)}
.problem-copy{left:624px;top:1196px;width:470px}
.problem-copy h2{font-size:36px;font-weight:600}
.problem-copy h2 b{font-weight:800}
.problem-copy p{margin:22px 0 34px;font-size:14px;line-height:1.8;color:var(--muted)}

/* audiences */
.audience{top:1592px;width:600px;height:496px;padding:90px 112px 0;color:var(--white)}
.audience.startups{left:0;background:linear-gradient(135deg,#3a3d40,var(--charcoal))}
.audience.tech{left:600px;background:linear-gradient(135deg,#1d7a89,var(--teal))}
.audience-head{display:flex;align-items:center;gap:18px}
.audience .icon{width:58px;height:58px;border-radius:50%;background:var(--white);display:flex;align-items:center;justify-content:center;flex:none}
.audience h3{font-size:28px;font-weight:700}
.audience p{margin:28px 0 44px;font-size:14px;line-height:1.8;color:rgba(255,255,255,.8);width:380px}

/* value */
.value{left:0;top:2168px;width:1200px;text-align:center}
.value h2{font-size:38px;font-weight:800}
.value h2 span{font-weight:400}
.value .sub{margin-top:14px;font-size:14px;color:var(--muted)}
.hub{left:0;top:2260px}
.benefit{width:300px}
.benefit h4{font-size:17px;font-weight:700;line-height:1.35}
.benefit p{margin-top:10px;font-size:13px;line-height:1.6;color:var(--muted)}
.benefit.left{text-align:right}
.hub-logo{left:510px;top:2350px;width:180px;height:180px;border-radius:50%;background:var(--white);display:flex;align-items:center;justify-content:center;gap:8px;font-size:28px}
.hub-logo .mark{width:20px;height:20px}
.benefit.bottom{left:450px;top:2680px;text-align:center}

/* testimonials */
.testimonials{left:0;top:2880px;width:1200px;height:370px;
  background:linear-gradient(120deg,#86c236 0%,var(--green) 45%,#5c9420 100%);
  clip-path:polygon(0 0,100% 0,100% 74%,50% 100%,0 74%);text-align:center;color:var(--white)}
.testimonials h2{margin-top:38px;font-size:32px;font-weight:800}
.testimonials .sub{font-size:13px;opacity:.9;margin-top:4px}
.stars{margin-top:16px;color:#ffd83a;font-size:16px;letter-spacing:3px}
.quote{width:660px;margin:10px auto 0;font-size:14px;line-height:1.7;opacity:.95}
.person{margin:18px auto 0;display:flex;align-items:center;justify-content:center;gap:14px;text-align:left}
.avatar{width:60px;height:60px;border-radius:50%;background:#cfd8dc;border:3px solid var(--white)}
.person b{display:block;font-size:14px}
.person small{font-size:12px;opacity:.9}
.t-arrow{top:110px;color:var(--white)}

/* footer */
.footer{left:0;top:3140px;width:1200px;height:568px;background:var(--footer);color:#c9cbcd}
.footer .brand{position:absolute;left:0;width:1200px;top:138px;justify-content:center;font-size:26px}
.footer .brand .mark{width:22px;height:22px}
.fcol{top:232px}
.fcol h4{font-size:15px;font-weight:700;color:var(--white);letter-spacing:.5px;margin-bottom:16px}
.fcol ul{list-style:none}
.fcol li{font-size:13px;line-height:26px;color:#b3b5b8}
.fcol li.contact{display:flex;align-items:center;gap:10px}
.fcol li.social{display:flex;align-items:center;gap:10px;margin-bottom:4px}
.soc{width:22px;height:22px;border-radius:50%;background:var(--blue)}
.copyright{left:0;top:530px;width:1200px;text-align:center;font-size:12px;color:#9a9c9f}
</style>
</head>
<body>
<div class="page">

  <div class="abs topline"></div>
  <header class="abs header">
    <a class="brand" href="#"><span class="mark"></span>lumatrel.io</a>
    <nav class="nav">
      <a class="active" href="#">HOME</a>
      <a href="#">SERVICES</a>
      <a href="#">RESOURCES</a>
      <a href="#">CONTACT US</a>
      <a href="#">BLOG</a>
      <a class="btn" href="#"><span class="dot"></span>LOGIN</a>
    </nav>
  </header>

  <section class="abs hero">
    <div class="hero-photo" role="img" aria-label="Photo of a business team meeting around a conference table in a bright office"></div>
    <svg class="abs hero-v" width="1200" height="660" viewBox="0 0 1200 660">
      <polygon points="0,500 600,628 1200,500 1200,660 0,660" fill="#ffffff"/>
      <polyline points="0,478 600,606 1200,478" fill="none" stroke="#1c96d4" stroke-width="4"/>
      <polyline points="0,488 600,616 1200,488" fill="none" stroke="#78b52a" stroke-width="4"/>
      <polyline points="0,498 600,626 1200,498" fill="none" stroke="#e3262d" stroke-width="5"/>
    </svg>
    <div class="abs hero-copy">
      <h1>A boutique digital agency helping high-tech startups accelerate growth</h1>
      <p>Lorem ipsum dolor sit amet, consectetur adipiscing elit, sed do eiusmod tempor incididunt magna aliqua.</p>
      <a class="btn" href="#">Get Started <span class="dot"><svg width="8" height="8" viewBox="0 0 8 8"><path d="M2 1l3 3-3 3" stroke="#f0421f" stroke-width="1.6" fill="none"/></svg></span></a>
    </div>
    <div class="abs hero-arrow" style="left:24px"><svg width="14" height="14" viewBox="0 0 14 14"><path d="M9 2L4 7l5 5" stroke="#333" stroke-width="2" fill="none"/></svg></div>
    <div class="abs hero-arrow" style="left:1136px"><svg width="14" height="14" viewBox="0 0 14 14"><path d="M5 2l5 5-5 5" stroke="#333" stroke-width="2" fill="none"/></svg></div>
  </section>

  <section class="abs welcome">
    <div class="mark-big"><span></span></div>
    <h2>Welcome To LumaTrel</h2>
    <p>We are a boutique team of engineers and technologists who build the digital infrastructure behind revenue operations. We align sales, marketing and customer success so growing technology companies can deliver extraordinary customer experiences across the full customer lifecycle and move at the speed of innovation.</p>
    <a class="btn" href="#">Read More <span class="dot"><svg width="8" height="8" viewBox="0 0 8 8"><path d="M2 1l3 3-3 3" stroke="#f0421f" stroke-width="1.6" fill="none"/></svg></span></a>
  </section>
  <div class="abs divider"></div>

  <div class="abs problem-photo" role="img" aria-label="Photo of colleagues working together at a long desk under pendant lights"></div>
  <section class="abs problem-copy">
    <h2><b>Problem</b> Statement</h2>
    <p>Technology founders build remarkable products, yet they often struggle to explain their value to the market. Complex innovation is hard to translate into clear messages, and disconnected sales, marketing and support tools leak revenue at every stage. Prospects lose interest, customers churn and growth stalls long before the product reaches its true potential.</p>
    <a class="btn" href="#">Read More <span class="dot"><svg width="8" height="8" viewBox="0 0 8 8"><path d="M2 1l3 3-3 3" stroke="#f0421f" stroke-width="1.6" fill="none"/></svg></span></a>
  </section>

  <section class="abs audience startups">
    <div class="audience-head">
      <span class="icon"><svg width="28" height="28" viewBox="0 0 28 28"><circle cx="14" cy="9" r="5" fill="#f0421f"/><path d="M4 25c0-6 4-9 10-9s10 3 10 9z" fill="#f0421f"/></svg></span>
      <h3>Entrepreneurial Startups</h3>
    </div>
    <p>Young companies need to move fast with lean teams. We set up the systems, automation and reporting that let founders focus on customers, shorten sales cycles and turn early traction into predictable, repeatable revenue growth without adding unnecessary overhead.</p>
    <a class="btn" href="#">Read More <span class="dot"><svg width="8" height="8" viewBox="0 0 8 8"><path d="M2 1l3 3-3 3" stroke="#f0421f" stroke-width="1.6" fill="none"/></svg></span></a>
  </section>
  <section class="abs audience tech">
    <div class="audience-head">
      <span class="icon"><svg width="28" height="28" viewBox="0 0 28 28"><circle cx="14" cy="14" r="6" fill="none" stroke="#f0421f" stroke-width="3"/><path d="M14 2v5M14 21v5M2 14h5M21 14h5M5.5 5.5l3.5 3.5M19 19l3.5 3.5M5.5 22.5L9 19M19 9l3.5-3.5" stroke="#f0421f" stroke-width="3"/></svg></span>
      <h3>Technology Sector</h3>
    </div>
    <p>Our engineers have worked with the technologies our clients bring to market. We understand complex products and help translate them into clear value stories, connected customer journeys and data-driven operations that support every stage of growth.</p>
    <a class="btn" href="#">Read More <span class="dot"><svg width="8" height="8" viewBox="0 0 8 8"><path d="M2 1l3 3-3 3" stroke="#f0421f" stroke-width="1.6" fill="none"/></svg></span></a>
  </section>

  <section class="abs value">
    <h2>value proposition <span>&amp; benefits</span></h2>
    <p class="sub">Everything we deliver is built around relentless customer focus and measurable growth.</p>
  </section>

  <svg class="abs hub" width="1200" height="460" viewBox="0 0 1200 460">
    <circle cx="600" cy="180" r="200" fill="none" stroke="#e6e6e6" stroke-width="2" stroke-dasharray="6 6"/>
    <circle cx="600" cy="180" r="104" fill="#ffffff" stroke="#e3262d" stroke-width="6"/>
    <circle cx="600" cy="180" r="118" fill="none" stroke="#f1f1f1" stroke-width="10"/>
    <g fill="#ffffff" stroke="#f0f0f0" stroke-width="6">
      <circle cx="405" cy="95" r="34"/><circle cx="795" cy="95" r="34"/>
      <circle cx="405" cy="290" r="34"/><circle cx="795" cy="290" r="34"/>
      <circle cx="600" cy="380" r="34"/>
    </g>
    <g fill="#e3262d">
      <circle cx="405" cy="95" r="27"/><circle cx="795" cy="95" r="27"/>
      <circle cx="405" cy="290" r="27"/><circle cx="795" cy="290" r="27"/>
      <circle cx="600" cy="380" r="27"/>
    </g>
    <g fill="none" stroke="#ffffff" stroke-width="2.5" stroke-linecap="round">
      <path d="M394 95l8 8 14-16"/>
      <path d="M784 103l8-8 6 5 10-12"/>
      <path d="M395 282h20v16h-20z"/>
      <circle cx="795" cy="290" r="10"/><path d="M795 284v6l4 3"/>
      <path d="M600 368l4 8 9 1-7 6 2 9-8-5-8 5 2-9-7-6 9-1z"/>
    </g>
  </svg>
  <div class="abs hub-logo brand"><span class="mark"></span>LumaTrel</div>

  <div class="abs benefit left" style="left:60px;top:2326px">
    <h4>Lorem ipsum dolor amet, consectetur</h4>
    <p>Aligned sales and marketing teams working as one.</p>
  </div>
  <div class="abs benefit" style="left:850px;top:2326px">
    <h4>Lorem ipsum dolor amet, consectetur</h4>
    <p>Automated journeys that respond to every customer.</p>
  </div>
  <div class="abs benefit left" style="left:60px;top:2522px">
    <h4>Lorem ipsum dolor amet, consectetur</h4>
    <p>Clear reporting on revenue across the lifecycle.</p>
  </div>
  <div class="abs benefit" style="left:850px;top:2522px">
    <h4>Lorem ipsum dolor amet, consectetur</h4>
    <p>Scalable systems that grow with your business.</p>
  </div>
  <div class="abs benefit bottom">
    <h4>Sed ut perspiciatis omnis</h4>
    <p>Memorable experiences that keep customers coming back.</p>
  </div>

  <footer class="abs footer">
    <svg class="abs" style="left:0;top:0" width="1200" height="130" viewBox="0 0 1200 130">
      <polyline points="0,14 600,120 1200,14" fill="none" stroke="#e3262d" stroke-width="4"/>
      <polyline points="0,22 600,128 1200,22" fill="none" stroke="#1c96d4" stroke-width="3"/>
    </svg>
    <a class="brand" href="#"><span class="mark"></span>lumatrel.io</a>

    <div class="abs fcol" style="left:112px">
      <h4>QUICK LINKS</h4>
      <ul><li>Homepage</li><li>Services</li><li>Resources</li><li>Contact Us</li><li>Blog</li></ul>
    </div>
    <div class="abs fcol" style="left:392px">
      <h4>INFORMATION</h4>
      <ul><li>Terms &amp; Conditions</li><li>Privacy Policy</li><li>Disclaimer</li><li>Site Map</li><li>Contact Us</li></ul>
    </div>
    <div class="abs fcol" style="left:612px">
      <h4>CONTACT INFO</h4>
      <ul>
        <li class="contact"><svg width="14" height="14" viewBox="0 0 14 14"><path d="M3 1l2.5 3-1.5 1.5c1 2 2.5 3.5 4.5 4.5L10 8.5l3 2.5-1.5 2C6 13 1 8 1 2.5z" fill="#78b52a"/></svg>(+230) 555 0142</li>
        <li class="contact"><svg width="14" height="14" viewBox="0 0 14 14"><path d="M3 1l2.5 3-1.5 1.5c1 2 2.5 3.5 4.5 4.5L10 8.5l3 2.5-1.5 2C6 13 1 8 1 2.5z" fill="#78b52a"/></svg>(+230) 555 0187</li>
        <li class="contact"><svg width="14" height="14" viewBox="0 0 14 14"><rect x="1" y="3" width="12" height="8" fill="none" stroke="#78b52a" stroke-width="1.5"/><path d="M1 3l6 5 6-5" fill="none" stroke="#78b52a" stroke-width="1.5"/></svg>hello@lumatrel.io</li>
        <li class="contact"><svg width="14" height="14" viewBox="0 0 14 14"><path d="M7 1a4 4 0 0 1 4 4c0 3-4 8-4 8S3 8 3 5a4 4 0 0 1 4-4z" fill="#78b52a"/><circle cx="7" cy="5" r="1.5" fill="#1d1e20"/></svg>24 Harbour Lane, Port Louis</li>
      </ul>
    </div>
    <div class="abs fcol" style="left:952px">
      <h4>FOLLOW US</h4>
      <ul>
        <li class="social"><span class="soc"></span>Newsroom</li>
        <li class="social"><span class="soc" style="background:#29a9e1"></span>Updates</li>
        <li class="social"><span class="soc" style="background:var(--red)"></span>Community</li>
        <li class="social"><span class="soc" style="background:#1a6fa8"></span>Network</li>
      </ul>
    </div>
    <p class="abs copyright">Copyright © LumaTrel 2024 | All Rights Reserved</p>
  </footer>

  <section class="abs testimonials">
    <h2>What our Cutomers Say?</h2>
    <p class="sub">Our clients tell our story</p>
    <div class="stars">★★★★★</div>
    <p class="quote">LumaTrel gave our team one clear view of every customer. Our sales cycle is shorter, our onboarding feels effortless and our revenue finally grows in a steady, predictable way.</p>
    <div class="person">
      <span class="avatar" role="img" aria-label="Client portrait photo"></span>
      <span><b>Daniel Rowe</b><small>Customer</small></span>
    </div>
    <svg class="abs t-arrow" style="left:112px" width="20" height="20" viewBox="0 0 20 20"><path d="M13 3L6 10l7 7" stroke="#fff" stroke-width="3" fill="none"/></svg>
    <svg class="abs t-arrow" style="left:1068px" width="20" height="20" viewBox="0 0 20 20"><path d="M7 3l7 7-7 7" stroke="#fff" stroke-width="3" fill="none"/></svg>
  </section>

</div>
</body>
</html>
```